Business Card Design Project

looking for business cards with new logo

I am looking to keep with the colors of the logo i posted.  Here are some other details to consider.  I would like my website prominently displayed on the business card with the logo.  my website is www.PRopelVK.com...it should be spelled this way.

My contact information is:

Daniel J Whitcombe III
Broker/Owner
4587 Larkspur Ave., Suite 308
Helotes, Texas 78023
Office: 830-419-5576
Email:  Daniel@PRopelVK.com

Thank you
Daniel Whitcombe

```html
<!DOCTYPE html>
<html lang="en">
<head>
<meta charset="utf-8">
<title>PRopelVK Business Card</title>
<link rel="stylesheet" href="https://fonts.googleapis.com/css2?family=Quicksand:wght@400;500&display=swap">
<style>
  :root {
    --brand-blue: #0071bc;
    --ink: #1a1a1a;
    --card-edge: #2b2b2b;
    --paper: #ffffff;
  }
  * { margin: 0; padding: 0; box-sizing: border-box; }
  html, body { width: 1000px; height: 1200px; overflow: hidden; background: var(--paper); }
  body { position: relative; font-family: "Quicksand", sans-serif; color: var(--ink); }

  .brand-mark {
    position: absolute; left: 0; width: 1000px; top: 170px;
    text-align: center; color: var(--brand-blue);
    font-size: 64px; font-weight: 400; letter-spacing: 1px; line-height: 1;
  }

  .card { position: absolute; border-radius: 22px; }
  .card-front {
    left: 43px; top: 360px; width: 432px; height: 620px;
    border: 1.5px solid var(--card-edge); background: var(--paper);
  }
  .card-back {
    left: 510px; top: 357px; width: 431px; height: 619px;
    background: var(--brand-blue);
  }

  .front-brand {
    position: absolute; top: 64px; left: 0; width: 100%;
    text-align: center; color: var(--brand-blue);
    font-size: 40px; font-weight: 400; line-height: 1;
  }

  .holder { position: absolute; left: 262px; top: 372px; width: 152px; text-align: center; }
  .holder-name {
    color: var(--brand-blue); font-size: 18px; font-weight: 400;
    padding-bottom: 6px; border-bottom: 2px solid var(--brand-blue); white-space: nowrap;
  }
  .holder-role { font-size: 15px; margin-top: 6px; }

  .contact { position: absolute; left: 16px; top: 468px; width: 244px; font-size: 12px; line-height: 17px; }
  .contact-row { display: flex; }
  .contact-label { width: 54px; flex: none; }
  .contact-colon { width: 10px; flex: none; }
  .contact-value { flex: 1; }

  .website {
    position: absolute; left: 0; width: 262px; top: 560px;
    text-align: center; font-size: 20px; font-weight: 500; color: var(--brand-blue);
    white-space: nowrap;
  }

  .accent-block {
    position: absolute; left: 274px; top: 462px; width: 136px; height: 134px;
    border-radius: 14px; background: var(--brand-blue);
  }

  .back-brand {
    position: absolute; left: 0; width: 100%; top: 334px;
    text-align: center; color: var(--paper);
    font-size: 52px; font-weight: 400; line-height: 1;
  }
</style>
</head>
<body>
  <div class="brand-mark">PRopelVK</div>

  <section class="card card-front">
    <div class="front-brand">PRopelVK</div>
    <div class="holder">
      <div class="holder-name">Daniel Whitcombe</div>
      <div class="holder-role">owner</div>
    </div>
    <div class="contact">
      <div class="contact-row"><span class="contact-label">email</span><span class="contact-colon">:</span><span class="contact-value">Daniel@PRopelVK.com</span></div>
      <div class="contact-row"><span class="contact-label">address</span><span class="contact-colon">:</span><span class="contact-value">4587 Larkspur Ave., Suite 308<br>Helotes, Texas 78023</span></div>
      <div class="contact-row"><span class="contact-label">phone</span><span class="contact-colon">:</span><span class="contact-value">830-419-5576</span></div>
    </div>
    <div class="accent-block"></div>
    <div class="website">www.PRopelVK.com</div>
  </section>

  <section class="card card-back">
    <div class="back-brand">PRopelVK</div>
  </section>
</body>
</html>
```